依頼詳細
■アプリの概要
作成中のiPhoneアプリは、「見出し散歩帖」というニュースまとめアプリです。各種新聞社が配信しているニュースを、新着順に読み比べることができます。新着順以外にも、人気順や新聞別に記事を読むこともできます。気になった記事を、ブックマークすることも可能です。全国紙だけでなく、スポーツ新聞の記事なども配信されます。

■アイコンのイメージ
「ひと目で新聞を扱ったアプリであることがわかるアイコン」をお願いしたいです。シンプルで、わかりやすいアイコンを希望しています。その他の点につきましては、作成者の方のセンスにおまかせしたいと考えております。

■注意点
iPhoneアプリアイコンの光沢・角丸はiOSが自動的に行なってくれるため、納品いただくファイルでは行わなくて結構です。
記載項目
サイズは以下のようにお願いします。

■アイコンのサイズ
1024 x 1024 px
144 x 144 px
114 x 114 px
72 x 72 px
57 x 57 px

■スプラッシュ画像
320 x 480 px
640 x 960 px
640 x 1136 px
768 x 1004 px
1536 x 2008 px
1024 x 748 px
2048 x 1496 px
希望イメージ
シンプル 複雑
単色 カラフル
暗い 明るい
日常 高級
遊び心 厳粛
未来的 伝統的
女性的 男性的
希望する色
特定の色は指定しませんが、派手ではなくある程度落ち着いた色でお願いします
納品ファイル
• イラストレーター形式 (.ai)
• フォトショップ形式 (.psd)
• PNG形式 (.png)
補足説明
アイコンのイメージには「ひと目で新聞を扱ったアプリであることがわかるアイコン」と書きましたが、これは新聞そのもののアイコンでなければいけないというわけではなく、「新聞」という言葉を入れるなどの方法で実現していただいても構いません。
すいません、スプラッシュ画像のサイズ指定に間違いがありましたので訂正させてください。

【誤】1024 x 748 px
【誤】2048 x 1496 px

【正】748 x 1024 px
【正】1496 x 2048 px

スプラッシュ画像はすべて縦長です。ご迷惑おかけします。
よろしくお願い致します。
■ 選んだ理由

新聞のアプリであることがわかりやすく伝わり、また、見た目も非常にシンプルかつ目を引くデザインで、目的に最も合致したものだったため選ばせて頂きました。とても満足しております。ありがとうございました。

■ 提案者全員のお礼・コメント

この度は、たくさんのご提案ありがとうございました。

```html
<!DOCTYPE html>
<html lang="ja">
<head>
<meta charset="utf-8">
<title>見出し散歩帖 スプラッシュとアイコン</title>
<link href="https://fonts.googleapis.com/css2?family=Shippori+Mincho:wght@500&display=swap" rel="stylesheet">
<style>
  :root {
    --page: #ffffff;
    --paper-light: #f6f1dc;
    --paper-mid: #efe7cb;
    --paper-deep: #e6dcba;
    --band: rgba(255, 255, 255, 0.75);
    --ink: #111111;
    --ink-soft: #8a8a8a;
    --arrow: #222222;
    --arrow-glyph: #ffffff;
    --mark-square: #9a9a9a;
  }
  html, body {
    margin: 0;
    padding: 0;
    width: 831px;
    height: 1200px;
    overflow: hidden;
    background: var(--page);
  }
  .canvas {
    position: relative;
    width: 831px;
    height: 1200px;
  }
  .splash {
    position: absolute;
    left: 116px;
    top: 33px;
    width: 599px;
    height: 847px;
    overflow: hidden;
  }
  .paper-art {
    position: absolute;
    inset: 0;
    background: radial-gradient(ellipse at 50% 45%, var(--paper-light) 0%, var(--paper-mid) 60%, var(--paper-deep) 100%);
  }
  .title-band {
    position: absolute;
    left: 0;
    right: 0;
    top: 410px;
    height: 90px;
    background: var(--band);
  }
  .nav-arrow {
    position: absolute;
    top: 432px;
    width: 46px;
    height: 46px;
  }
  .nav-arrow.prev { left: 83px; }
  .nav-arrow.next { left: 471px; }
  .app-title {
    position: absolute;
    left: 256px;
    top: 300px;
    margin: 0;
    writing-mode: vertical-rl;
    font-family: "Shippori Mincho", serif;
    font-weight: 500;
    font-size: 56px;
    line-height: 1;
    letter-spacing: 3px;
    color: var(--ink);
  }
  .app-title .in-band { color: var(--ink-soft); }
  .app-mark {
    position: absolute;
    left: 300px;
    top: 1050px;
    width: 232px;
    height: 40px;
    display: flex;
    align-items: center;
    gap: 12px;
  }
  .app-mark-square {
    width: 32px;
    height: 32px;
    background: var(--mark-square);
    flex: none;
  }
  .app-mark-name {
    font-family: "Shippori Mincho", serif;
    font-weight: 500;
    font-size: 30px;
    line-height: 1;
    color: var(--ink);
    white-space: nowrap;
  }
</style>
</head>
<body>
<main class="canvas">
  <section class="splash">
    <div class="paper-art" role="img" aria-label="重ねて散らばった新聞紙のイラスト"></div>
    <div class="title-band"></div>
    <svg class="nav-arrow prev" viewBox="0 0 46 46" role="img" aria-label="前へ">
      <circle cx="23" cy="23" r="22" fill="var(--arrow)"/>
      <path d="M15 23 L29 14 L29 32 Z" fill="var(--arrow-glyph)"/>
    </svg>
    <svg class="nav-arrow next" viewBox="0 0 46 46" role="img" aria-label="次へ">
      <circle cx="23" cy="23" r="22" fill="var(--arrow)"/>
      <path d="M31 23 L17 14 L17 32 Z" fill="var(--arrow-glyph)"/>
    </svg>
    <h1 class="app-title">見出<span class="in-band">し散</span>歩帖</h1>
  </section>

  <div class="app-mark">
    <span class="app-mark-square" aria-hidden="true"></span>
    <span class="app-mark-name">見出し散歩帖</span>
  </div>
</main>
</body>
</html>
```